Tolliver Business Services Stationary
Letterhead, Business Card, Envelope
Tolliver Business Services Stationary -
Creative Brief
Simple
Dale Pruett
Bookkeeping and Tax Preparation
PO Box 4713 Seattle, WA 98109
dpruettpruett@tolliverllc.example
www.tolliverllc.example
The info for the business card is fake because this is not a private contest. I will provide the correct info when I finalize the contest. I need a standard sized business card, letterhead, and envelope. Finished artwork needs to be vector format. I have attached designs that I like and my company logo.
Maybe just the logo? reversed colors? I've attached samples and layouts the I like.

```html
<!DOCTYPE html>
<html lang="en">
<head>
<meta charset="utf-8">
<title>Tolliver Business Services Stationery</title>
<link href="https://fonts.googleapis.com/css2?family=Open+Sans:wght@400;600&display=swap" rel="stylesheet">
<style>
:root{
  --bg:#d6d6d6;
  --paper:#ffffff;
  --ink:#3a3a3a;
  --ink-soft:#777777;
  --dark:#363636;
  --mid:#8c8c8c;
  --rule:#cfcfcf;
  --on-dark:#ffffff;
}
*{margin:0;padding:0;box-sizing:border-box}
html,body{width:1200px;height:785px;overflow:hidden}
body{background:var(--bg);font-family:"Open Sans",Arial,sans-serif;color:var(--ink);position:relative}
.sheet{position:absolute;background:var(--paper);box-shadow:0 2px 6px rgba(0,0,0,.18);overflow:hidden}
.brand{display:flex;align-items:center;gap:8px}
.brand-mark{display:block;background:var(--ink);flex:none}
.brand-name{font-family:"Open Sans",Arial,sans-serif;font-weight:600;text-transform:uppercase;letter-spacing:.06em;color:var(--ink);line-height:1}
.brand-sub{font-size:6px;letter-spacing:.12em;text-transform:uppercase;color:var(--ink-soft);margin-top:3px}
.tiny{font-size:6.5px;line-height:1.5;color:var(--ink-soft)}

/* Letterhead */
.letterhead{left:125px;top:72px;width:440px;height:636px}
.letterhead .brand{position:absolute;left:28px;top:26px}
.letterhead .brand-mark{width:22px;height:22px}
.letterhead .brand-name{font-size:21px}
.letterhead .head-contact{position:absolute;right:30px;top:34px;text-align:left}
.letter-body{position:absolute;left:24px;top:88px;width:392px;font-size:6.5px;line-height:1.55;color:var(--ink-soft)}
.letter-body p{margin-bottom:8px}
.recipient{margin-bottom:18px}
.salutation{margin-bottom:10px}
.signature{width:40px;height:18px;background:linear-gradient(90deg,#e6e6e6,#c9c9c9);margin:6px 0 4px;border-radius:2px}
.letter-foot{position:absolute;left:24px;top:528px}
.letter-band-light{position:absolute;left:0;bottom:26px;width:100%;height:6px;background:var(--mid)}
.letter-band{position:absolute;left:0;bottom:0;width:100%;height:26px;background:var(--dark)}

/* Business cards */
.card{top:96px;height:72px}
.card-front{left:607px;width:128px;background:var(--dark);display:flex;align-items:center;justify-content:center}
.card-front .brand-mark{width:14px;height:14px;background:var(--on-dark)}
.card-back{left:751px;width:156px}
.card-back .brand{position:absolute;left:10px;top:10px;gap:5px}
.card-back .brand-mark{width:10px;height:10px}
.card-back .brand-name{font-size:10px}
.card-back .tiny{font-size:4px;line-height:1.5}
.card-person{position:absolute;left:10px;top:38px;width:54px}
.card-contact{position:absolute;right:8px;top:34px;white-space:nowrap}

/* Envelope front */
.envelope-front{left:619px;top:216px;width:468px;height:228px}
.envelope-front .brand{position:absolute;left:22px;top:30px}
.envelope-front .brand-mark{width:20px;height:20px}
.envelope-front .brand-name{font-size:19px}
.envelope-front .return-address{position:absolute;left:26px;top:86px}
.envelope-band{position:absolute;left:0;bottom:0;width:100%;height:22px;background:var(--dark)}

/* Envelope back */
.envelope-back{left:619px;top:463px;width:468px;height:221px}
.envelope-back svg{position:absolute;left:0;top:0}
.flap-contact{position:absolute;left:328px;top:22px;display:flex;align-items:center;gap:6px}
.flap-contact .brand-mark{width:9px;height:9px;background:var(--on-dark)}
.flap-contact .tiny{color:var(--on-dark);font-size:5.5px}
</style>
</head>
<body>

<section class="sheet letterhead" aria-label="Letterhead">
  <div class="brand">
    <span class="brand-mark"></span>
    <div>
      <div class="brand-name">Tolliver</div>
      <div class="brand-sub">Business Services</div>
    </div>
  </div>
  <div class="head-contact tiny">
    dpruettpruett@tolliverllc.example<br>
    www.tolliverllc.example
  </div>
  <div class="letter-body">
    <p class="recipient">Ms. Reader<br>Accounting Manager<br>Seattle, WA 98101</p>
    <p class="salutation">Dear Client Name,</p>
    <p>Thank you for choosing our office for your bookkeeping and tax preparation needs this year. We have reviewed the documents you sent and prepared a short summary of the next steps for your accounts. Please look over the enclosed forms, sign where marked, and return them at your convenience.</p>
    <p>Our team keeps careful records through every quarter so that filing season runs smoothly. If anything in the summary looks unclear, call or write and we will walk through each item with you in plain terms.</p>
    <p>We look forward to working with you again and appreciate your continued trust in our services.</p>
    <p style="margin-top:14px;margin-bottom:0">Thank you,</p>
    <div class="signature" role="img" aria-label="Handwritten signature"></div>
    <p>Dale Pruett</p>
  </div>
  <div class="letter-foot tiny">
    PO Box 4713<br>
    Seattle, WA 98109<br>
    dpruettpruett@tolliverllc.example<br>
    www.tolliverllc.example
  </div>
  <div class="letter-band-light"></div>
  <div class="letter-band"></div>
</section>

<section class="sheet card card-front" aria-label="Business card front">
  <div class="brand">
    <span class="brand-mark"></span>
  </div>
</section>

<section class="sheet card card-back" aria-label="Business card back">
  <div class="brand">
    <span class="brand-mark"></span>
    <span class="brand-name">Tolliver</span>
  </div>
  <div class="card-person tiny">
    Dale Pruett<br>
    Bookkeeping and<br>Tax Preparation
  </div>
  <div class="card-contact tiny">
    PO Box 4713<br>
    Seattle, WA 98109<br>
    dpruettpruett@tolliverllc.example<br>
    www.tolliverllc.example
  </div>
</section>

<section class="sheet envelope-front" aria-label="Envelope front">
  <div class="brand">
    <span class="brand-mark"></span>
    <div>
      <div class="brand-name">Tolliver</div>
      <div class="brand-sub">Business Services</div>
    </div>
  </div>
  <div class="return-address tiny">
    PO Box 4713<br>
    Seattle, WA 98109
  </div>
  <div class="envelope-band"></div>
</section>

<section class="sheet envelope-back" aria-label="Envelope back">
  <svg width="468" height="221" viewBox="0 0 468 221">
    <line x1="0" y1="221" x2="200" y2="118" stroke="var(--rule)" stroke-width="1"/>
    <line x1="468" y1="221" x2="268" y2="118" stroke="var(--rule)" stroke-width="1"/>
    <polygon points="0,0 468,0 468,64 234,102 0,64" fill="var(--dark)"/>
  </svg>
  <div class="flap-contact">
    <span class="brand-mark"></span>
    <div class="tiny">
      dpruettpruett@tolliverllc.example<br>
      www.tolliverllc.example
    </div>
  </div>
</section>

</body>
</html>
```